Create an Animation cell phone text message

I am finishing up a design of my website http://plinkworth.org/demo/marcus/tallydesk3/index.htmlm slide one has a cell phone come up with static text, i would like the text to change in the phone.
I have added a couple cell phone templates to use. Use what everone works best for you.
The messages I would like to rotate are:
Welcome to Your College, You will receive a text message when it is your turn. You are 12 in the registration line, reply T for more Time or S for Status

No ticket machines, printers or even smart phones required, customers text simple commands to manage their place in virtual line.

Studies show, 24% of consumers abandon their purchases, when confronted with long (physical) waiting lines.

According to the Halvern Consortium for Merchant Studies, the average customer spends about $1 dollar per minute while shopping.

Customers are no longer tethered to long physical lines, they are free to spend money while in a virtual waiting line.

Improved customer flow increases customer satisfaction and loyalty.

Families love visiting Santa at the mall without the long wait in line.

```html
<!DOCTYPE html>
<html lang="en">
<head>
<meta charset="utf-8">
<title>Santa's Little Helper – Text Messages</title>
<link rel="stylesheet" href="https://fonts.googleapis.com/css2?family=Open+Sans:wght@400;600&display=swap">
<style>
  :root {
    --page-bg: #e3e3e3;
    --phone-body: #141414;
    --phone-rim: #3a3a3a;
    --phone-key: #5a5a5a;
    --screen-bg: #ececec;
    --status-bg: #0d0d0d;
    --status-blue: #35b5e5;
    --header-text: #1e1e1e;
    --meta-text: #7a7a7a;
    --bubble: #574c8c;
    --bubble-edge: #4a4079;
    --bubble-gloss: rgba(255,255,255,0.26);
    --bubble-text: #ffffff;
  }
  * { margin: 0; padding: 0; box-sizing: border-box; }
  html, body {
    width: 1200px; height: 675px; overflow: hidden;
    background: var(--page-bg);
    font-family: "Open Sans", Arial, sans-serif;
  }
  .canvas { position: relative; width: 1200px; height: 675px; }
  .phone-body { position: absolute; left: 0; top: 0; }
  .message-screen {
    position: absolute; left: 461px; top: 117px;
    width: 279px; height: 466px;
    background: var(--screen-bg);
    overflow: hidden;
  }
  .status-bar {
    height: 22px; background: var(--status-bg);
    display: flex; align-items: center; justify-content: space-between;
    padding: 0 6px;
  }
  .status-right { display: flex; align-items: center; gap: 5px; }
  .status-time { color: var(--status-blue); font-size: 14px; line-height: 1; }
  .thread-header { text-align: center; padding-top: 3px; }
  .thread-title { font-size: 11px; font-weight: 600; color: var(--header-text); line-height: 15px; }
  .thread-meta { font-size: 9px; color: var(--meta-text); line-height: 11px; }
  .bubble {
    position: absolute; left: 16px; width: 240px;
    background: var(--bubble);
    border: 1px solid var(--bubble-edge);
    border-radius: 15px;
    color: var(--bubble-text);
    font-size: 16.4px; line-height: 23px; letter-spacing: -0.15px;
    white-space: nowrap;
    padding: 6px 8px 0 19px;
    overflow: hidden;
  }
  .bubble::before {
    content: ""; position: absolute; left: 12px; top: 3px;
    width: 210px; height: 24px; border-radius: 12px;
    background: var(--bubble-gloss);
  }
  .bubble-text { position: relative; }
  .bubble-welcome { top: 82px; height: 162px; }
  .bubble-commands { top: 272px; height: 164px; }
</style>
</head>
<body>
<main class="canvas">
  <svg class="phone-body" width="1200" height="675" viewBox="0 0 1200 675" aria-hidden="true">
    <defs>
      <linearGradient id="bodyShade" x1="0" y1="0" x2="1" y2="0">
        <stop offset="0" stop-color="#2a2a2a"/>
        <stop offset="0.5" stop-color="#141414"/>
        <stop offset="1" stop-color="#2a2a2a"/>
      </linearGradient>
      <radialGradient id="dropShadow" cx="0.5" cy="0.5" r="0.5">
        <stop offset="0" stop-color="#000" stop-opacity="0.35"/>
        <stop offset="1" stop-color="#000" stop-opacity="0"/>
      </radialGradient>
    </defs>
    <ellipse cx="600" cy="660" rx="190" ry="14" fill="url(#dropShadow)"/>
    <rect x="430" y="118" width="6" height="90" rx="2" fill="#2b2b2b"/>
    <rect x="764" y="140" width="5" height="50" rx="2" fill="#2b2b2b"/>
    <rect x="433" y="24" width="334" height="636" rx="66" fill="var(--phone-rim)"/>
    <rect x="437" y="28" width="326" height="628" rx="62" fill="url(#bodyShade)"/>
    <rect x="561" y="65" width="78" height="8" rx="4" fill="#2e2e2e" stroke="#444" stroke-width="1"/>
    <circle cx="506" cy="69" r="4" fill="#2c2c2c"/>
    <circle cx="527" cy="69" r="4" fill="#2c2c2c"/>
    <rect x="457" y="113" width="287" height="474" rx="3" fill="#050505"/>
    <g fill="none" stroke="var(--phone-key)" stroke-width="2.5" stroke-linecap="round" stroke-linejoin="round">
      <path d="M492 613 h12 a5 5 0 0 1 0 10 h-4"/>
      <path d="M497 608 l-5 5 l5 5"/>
      <path d="M556 608 h22 M556 613 h22 M556 618 h22"/>
      <circle cx="627" cy="611" r="5.5"/>
      <path d="M631 615 l6 6"/>
      <path d="M684 616 l12 -9 l12 9 M688 614 v8 h16 v-8"/>
    </g>
  </svg>

  <section class="message-screen">
    <div class="status-bar">
      <svg width="14" height="12" viewBox="0 0 14 12" aria-hidden="true">
        <rect x="0" y="9" width="2.5" height="3" fill="#35b5e5"/>
        <rect x="3.5" y="6" width="2.5" height="6" fill="#35b5e5"/>
        <rect x="7" y="3" width="2.5" height="9" fill="#35b5e5"/>
        <rect x="10.5" y="0" width="2.5" height="12" fill="#35b5e5"/>
      </svg>
      <div class="status-right">
        <svg width="8" height="12" viewBox="0 0 8 12" aria-hidden="true">
          <rect x="0" y="5" width="2.5" height="7" fill="#8a8a8a"/>
          <rect x="4.5" y="1" width="2.5" height="11" fill="#8a8a8a"/>
        </svg>
        <svg width="8" height="14" viewBox="0 0 8 14" aria-hidden="true">
          <rect x="2" y="0" width="4" height="2" fill="#35b5e5"/>
          <rect x="0.5" y="2" width="7" height="11.5" fill="none" stroke="#35b5e5"/>
          <rect x="1.5" y="5" width="5" height="7.5" fill="#35b5e5"/>
        </svg>
        <span class="status-time">2:56</span>
      </div>
    </div>
    <header class="thread-header">
      <div class="thread-title">Santa's Little Helper</div>
      <div class="thread-meta">Text Messages</div>
      <div class="thread-meta">25 Dec</div>
    </header>
    <div class="bubble bubble-welcome">
      <p class="bubble-text">Welcome to Your College,<br>You will receive a text<br>message when it is your<br>turn. You are 12 in the<br>registration line, reply T for<br>more Time or S for Status</p>
    </div>
    <div class="bubble bubble-commands">
      <p class="bubble-text">No ticket machines,<br>printers or even smart<br>phones required,<br>customers text simple<br>commands to manage<br>their place in virtual line.</p>
    </div>
  </section>
</main>
</body>
</html>
```